Creative Businesss Card desgin!

Create a business card for our business Gleam window cleaning!
We are open to creative ideas as long as it maintains a professional image.

Target Market(s)

Small Commercial window cleaning clients including car dealerships, strata manager, cafe

Industry/Entity Type

Window Cleaning

Contact Information for Business Card

Daniel Prescott
General Manager
Gleam Window Cleaning

daniel@gleamservices.com.au
pane-care-southbank.com.au
Ph: 1800 GET GLEAM
Mob: 0437 582 061

Colors
fbed22
0392cd

Requirements
Should not have
• Stock window cleaning/ squeegee graphics

```html
<!DOCTYPE html>
<html lang="en">
<head>
<meta charset="utf-8">
<title>Gleam Window Cleaning – Business Card</title>
<link href="https://fonts.googleapis.com/css2?family=Roboto:wght@400;500;700&family=Roboto+Condensed:wght@700&display=swap" rel="stylesheet">
<style>
  :root {
    --backdrop: #2a2a2a;
    --card-blue: #0d5585;
    --pattern-blue: #1a5f80;
    --gleam-yellow: #f2ec22;
    --text-white: #f2f4f6;
    --title-grey: #dfe6ec;
  }
  * { margin: 0; padding: 0; box-sizing: border-box; }
  html, body {
    width: 1200px; height: 960px; overflow: hidden;
    background: var(--backdrop);
    font-family: "Roboto", Arial, sans-serif;
  }
  .stage { position: relative; width: 1200px; height: 960px; }

  .card {
    position: absolute;
    width: 600px; height: 343px;
    background: var(--card-blue);
    overflow: hidden;
  }
  .card--front { left: 314px; top: 113px; }
  .card--back  { left: 311px; top: 472px; }

  /* Front: contact block */
  .contact {
    position: absolute; right: 33px; top: 38px;
    text-align: right; color: var(--text-white);
  }
  .contact__name {
    font-family: "Roboto Condensed", "Arial Narrow", sans-serif;
    font-weight: 700; font-size: 23px; line-height: 26px;
    color: var(--gleam-yellow); letter-spacing: 0.2px;
  }
  .contact__title {
    font-size: 15px; font-weight: 500; line-height: 18px;
    color: var(--title-grey); letter-spacing: 0.3px;
  }
  .contact__company { margin-top: 16px; font-size: 14.5px; line-height: 19px; }
  .contact__line {
    display: flex; justify-content: flex-end; align-items: center;
    font-size: 14.5px; line-height: 19.5px;
  }
  .contact__icon { width: 14px; height: 14px; margin-left: 7px; flex: none; }
  .accent-tab {
    position: absolute; right: 0; top: 40px;
    width: 9px; height: 40px; background: var(--gleam-yellow);
  }

  /* Front: wordmark */
  .wordmark {
    position: absolute; left: 36px; top: 204px;
    color: var(--gleam-yellow); font-weight: 700;
    font-family: "Roboto", Arial, sans-serif;
  }
  .wordmark__name { font-size: 56px; line-height: 56px; letter-spacing: 1px; }
  .wordmark__sub { font-size: 18.5px; line-height: 24px; margin-top: 2px; }

  /* Front: web band */
  .web-band { position: absolute; left: 0; top: 296px; width: 600px; height: 30px; }
  .web-band__url {
    position: absolute; left: 36px; top: 300px;
    font-size: 15px; line-height: 20px; letter-spacing: 2px;
    color: var(--card-blue); font-weight: 500;
  }

  /* Back */
  .pattern-field { position: absolute; inset: 0; background: var(--pattern-blue); opacity: 0.55; }
  .back-mark {
    position: absolute; left: 0; right: 0; top: 130px;
    text-align: center; color: var(--gleam-yellow);
    font-weight: 700; font-size: 60px; line-height: 64px; letter-spacing: 2px;
  }
  .back-url {
    position: absolute; left: 0; right: 0; top: 287px;
    text-align: center; color: var(--text-white);
    font-size: 15px; letter-spacing: 2px;
  }
</style>
</head>
<body>
<main class="stage">

  <section class="card card--front" aria-label="Business card front">
    <div class="accent-tab"></div>
    <div class="contact">
      <p class="contact__name">DANIEL PRESCOTT</p>
      <p class="contact__title">GENERAL MANAGER</p>
      <p class="contact__company">Gleam Window Cleaning</p>
      <p class="contact__line">1800 GET GLEAM
        <svg class="contact__icon" viewBox="0 0 24 24" aria-hidden="true"><path fill="#f2ec22" d="M6.6 10.8c1.4 2.8 3.8 5.1 6.6 6.6l2.2-2.2c.3-.3.7-.4 1-.2 1.1.4 2.3.6 3.6.6.6 0 1 .4 1 1V20c0 .6-.4 1-1 1C10.6 21 3 13.4 3 4c0-.6.4-1 1-1h3.5c.6 0 1 .4 1 1 0 1.3.2 2.5.6 3.6.1.3 0 .7-.2 1l-2.3 2.2z"/></svg>
      </p>
      <p class="contact__line">0437 582 061
        <svg class="contact__icon" viewBox="0 0 24 24" aria-hidden="true"><rect x="6" y="2" width="12" height="20" rx="2" fill="none" stroke="#f2ec22" stroke-width="2.4"/><rect x="10.5" y="17.5" width="3" height="1.6" fill="#f2ec22"/></svg>
      </p>
      <p class="contact__line">daniel@gleamservices.com.au
        <svg class="contact__icon" viewBox="0 0 24 24" aria-hidden="true"><rect x="2" y="5" width="20" height="14" fill="#f2ec22"/><path d="M2 5l10 8 10-8" fill="none" stroke="#0d5585" stroke-width="1.8"/></svg>
      </p>
    </div>

    <div class="wordmark">
      <p class="wordmark__name">GLEAM</p>
      <p class="wordmark__sub">WINDOW CLEANING</p>
    </div>

    <svg class="web-band" viewBox="0 0 600 30" aria-hidden="true">
      <polygon points="0,4 545,0 552,26 0,26" fill="#f2ec22"/>
      <rect x="540" y="6" width="16" height="16" fill="#f2ec22"/>
    </svg>
    <p class="web-band__url">www.pane-care-southbank.com.au</p>
  </section>

  <section class="card card--back" aria-label="Business card back">
    <div class="pattern-field" role="img" aria-label="Repeating pattern of faint brand marks across the card"></div>
    <p class="back-mark">GLEAM</p>
    <p class="back-url">www.pane-care-southbank.com.au</p>
  </section>

</main>
</body>
</html>
```